Dorian Name Card Design

I would like to have a name card with these information:
Name on Card: Dorian Pelzeck
Job: General Director
Company: BRULENTIX., JSC (BRULENTIX HEAVY EQUIPMENT FABRICATION JOINT STOCK COMPANY)
Address: 7318 Quillfern Dr. ,San Antonio, Texas, US
Tel: 2105497260
Email: DorianPelzeck@brulentix.example
Job: General Director
Tel: 2105497260

Industry/Entity Type

Construction

Requirements
Must have
• Name on Card: Dorian Pelzeck
• Job: General Director
• Company: BRULENTIX., JSC (BRULENTIX HEAVY EQUIPMENT FABRICATION JOINT STOCK COMPANY)
• Address: 7318 Quillfern Dr. ,San Antonio, Texas, US
• Tel: 2105497260
• Email: DorianPelzeck@brulentix.example
Nice to have
• Job: General Director
• Tel: 2105497260
Should not have
• Logo

```html
<!DOCTYPE html>
<html lang="en">
<head>
<meta charset="utf-8">
<title>Dorian Pelzeck — Name Card</title>
<link rel="stylesheet" href="https://fonts.googleapis.com/css2?family=Oswald:wght@300;400&family=Poiret+One&display=swap">
<style>
  :root {
    --ink: #3b484c;
    --ink-soft: #4a575b;
    --paper-light: #fbfcfc;
    --paper-mid: #eef1f1;
    --paper-deep: #e4e8e8;
    --band-fill: #e3eae8;
    --band-edge-top: #cfd8d6;
    --band-edge-bottom: #4d5a5d;
  }
  * { margin: 0; padding: 0; box-sizing: border-box; }
  html, body {
    width: 1200px;
    height: 720px;
    overflow: hidden;
    background: #ffffff;
  }
  .name-card {
    position: relative;
    width: 1200px;
    height: 720px;
    overflow: hidden;
    color: var(--ink);
    font-family: "Oswald", "Arial Narrow", sans-serif;
  }
  .card-backdrop {
    position: absolute;
    inset: 0;
    background:
      radial-gradient(ellipse at 20% 70%, var(--paper-deep) 0%, transparent 55%),
      linear-gradient(135deg, var(--paper-mid) 0%, var(--paper-light) 45%, var(--paper-mid) 100%);
  }
  .header-band {
    position: absolute;
    left: 0;
    top: 146px;
    width: 1200px;
    height: 156px;
    background: var(--band-fill);
    border-top: 2px solid var(--band-edge-top);
    border-bottom: 3px solid var(--band-edge-bottom);
  }
  .company-name {
    position: absolute;
    left: 112px;
    top: 146px;
    font-size: 44px;
    font-weight: 400;
    letter-spacing: -0.5px;
    line-height: 1.2;
    white-space: nowrap;
  }
  .company-fullname {
    position: absolute;
    left: 112px;
    top: 206px;
    font-size: 26px;
    font-weight: 300;
    line-height: 32px;
    letter-spacing: -0.6px;
    text-transform: uppercase;
    color: var(--ink-soft);
  }
  .person-name {
    position: absolute;
    right: 44px;
    top: 148px;
    font-family: "Poiret One", "Century Gothic", sans-serif;
    font-size: 68px;
    font-weight: 400;
    letter-spacing: 3px;
    line-height: 1.1;
    text-transform: uppercase;
    white-space: nowrap;
  }
  .person-title {
    position: absolute;
    left: 730px;
    width: 320px;
    top: 212px;
    text-align: center;
    font-size: 46px;
    font-weight: 400;
    letter-spacing: -0.5px;
    line-height: 1.2;
    white-space: nowrap;
  }
  .contact-list {
    position: absolute;
    left: 752px;
    top: 394px;
    list-style: none;
    font-weight: 300;
    font-size: 35px;
    line-height: 43px;
    letter-spacing: -0.6px;
  }
  .contact-item {
    display: flex;
    white-space: nowrap;
  }
  .contact-label {
    width: 46px;
    flex: none;
  }
  .contact-value--email {
    font-size: 28px;
    letter-spacing: -0.4px;
  }
</style>
</head>
<body>
  <main class="name-card">
    <div class="card-backdrop" role="img" aria-label="Soft white and pale grey diamond lattice background"></div>
    <div class="header-band" role="img" aria-label="Horizontal band with a fine pale grey crosshatch texture"></div>

    <h2 class="company-name">BRULENTIX., JSC</h2>
    <p class="company-fullname">(Brulentix Heavy Equipment<br>Fabrication Joint Stock<br>Company)</p>

    <h1 class="person-name">Dorian Pelzeck</h1>
    <p class="person-title">GENERAL DIRECTOR</p>

    <ul class="contact-list">
      <li class="contact-item"><span class="contact-label">P.</span><span class="contact-value">2105497260</span></li>
      <li class="contact-item"><span class="contact-label">A.</span><span class="contact-value">7318 QUILLFERN<br>DR.SAN ANTONIO<br>TEXAS,US.</span></li>
      <li class="contact-item"><span class="contact-label">E.</span><span class="contact-value contact-value--email">DorianPelzeck@brulentix.example</span></li>
    </ul>
  </main>
</body>
</html>
```